Car Loan Landing Page Redesign

We are looking for a fresh, eye catching and professional redesign of our landing page as attached.
This current template doesn't stand out and doesn't highlight the main part of the page which is the application box.
Our corporate colors are pink #ee245f, black #000, #232323 and colors as in our website www.brindlecove.com.au
Brindle is Australia's leading car finance brokerage institution and this landing page is geared towards car finance.
We also believe the background banner needs some sort of creative approach.
We also feel that the form steps (once you click on start to compare) needs to be refreshed as well in terms of its form input fields design.
We like to have this whole page redesigned and freshen up so it gives an unique design experience to the users.
Feel free to use your imagination with some great eye catchy banner, and move the elements around as you need to.
Target Market(s)
Australians who are looking for car finance
Industry/Entity Type
Finance
Number of Pages Required
1 page
Font styles to use
Other font styles liked:
- Roboto
Look and feel

```html
<!DOCTYPE html>
<html lang="en">
<head>
<meta charset="utf-8">
<title>Brindle Car Loans</title>
<link href="https://fonts.googleapis.com/css2?family=Roboto:wght@300;400;500;700&display=swap" rel="stylesheet">
<style>
:root{
  --pink:#ee245f;
  --pink-dark:#e81b57;
  --ink:#232323;
  --text:#444;
  --muted:#777;
  --light-bg:#f3f3f3;
  --white:#fff;
  --line:#d8d8d8;
}
*{box-sizing:border-box;margin:0;padding:0}
html,body{width:1200px;height:2951px;overflow:hidden}
body{font-family:'Roboto',Arial,sans-serif;color:var(--text);background:var(--white);position:relative}
.abs{position:absolute}

/* hero */
.hero{position:absolute;left:0;top:0;width:1200px;height:590px;background:linear-gradient(160deg,#6b7268 0%,#8d948c 35%,#b6bbb8 60%,#7c827f 100%)}
.hero-shade{position:absolute;inset:0;background:rgba(0,0,0,.28)}
.brand{position:absolute;left:122px;top:40px;display:flex;align-items:center;gap:10px;color:var(--white);font-size:34px;font-weight:500;line-height:1}
.brand-mark{width:22px;height:22px;background:var(--pink);display:block}
.hero-note{position:absolute;left:334px;top:60px;color:var(--white);font-size:13px}
.hero-phone{position:absolute;left:888px;top:48px;color:var(--white);font-size:25px;display:flex;align-items:center;gap:8px}
.hero-title{position:absolute;left:0;width:1200px;top:235px;text-align:center;color:var(--white);font-size:38px;font-weight:400}
.hero-sub{position:absolute;left:0;width:1200px;top:296px;text-align:center;color:var(--white);font-size:25px;font-weight:500}
.hero-arrow{position:absolute;top:262px}

/* steps */
.steps{position:absolute;left:0;top:590px;width:1200px;height:510px;background:var(--light-bg)}
.step{position:absolute;width:260px;text-align:center;top:-60px}
.step-badge{width:134px;height:134px;border-radius:50%;background:var(--white);margin:0 auto;display:flex;align-items:center;justify-content:center;box-shadow:0 2px 6px rgba(0,0,0,.08)}
.step-badge span{width:118px;height:118px;border-radius:50%;background:var(--pink);display:flex;align-items:center;justify-content:center}
.step-title{color:var(--pink);font-size:25px;font-weight:500;margin-top:20px}
.step-desc{font-size:14px;color:var(--muted);line-height:1.45;margin-top:10px}

.tablet{position:absolute;left:309px;top:205px;width:578px;height:305px;border:3px solid #cfcfcf;border-bottom:none;border-radius:22px 22px 0 0;background:#fafafa}
.screen{position:absolute;left:38px;top:38px;width:497px;height:264px;background:var(--white);border:1px solid #e4e4e4;border-bottom:none;text-align:center}
.screen-q{font-size:23px;color:#555;font-weight:300;margin-top:28px}
.amount{width:148px;height:40px;border:1px solid #ccc;margin:22px auto 0;font-size:25px;color:#444;line-height:38px;background:#fdfdfd}
.slider{position:absolute;left:46px;top:147px;width:416px;height:6px;background:#e9e9e9}
.slider-knob{position:absolute;left:-9px;top:-7px;width:20px;height:20px;border-radius:50%;background:var(--pink)}
.ticks{position:absolute;left:40px;top:168px;width:426px;display:flex;justify-content:space-between;font-size:8px;color:#999}
.btn{display:inline-block;background:var(--pink);color:var(--white);border-radius:24px;font-weight:500}
.screen .btn{position:absolute;left:160px;top:213px;width:178px;height:40px;line-height:40px;font-size:15px}
.side-icons{position:absolute;left:14px;top:120px;display:flex;flex-direction:column;gap:22px}
.side-icons i{width:8px;height:8px;border:1px solid #bbb;border-radius:2px;display:block}
.home-key{position:absolute;right:14px;top:165px;width:6px;height:48px;background:#555;border-radius:3px}

/* lenders */
.lenders{position:absolute;left:0;top:1100px;width:1200px;height:366px;background:var(--white);text-align:center}
.lenders h2{font-size:31px;font-weight:400;color:var(--ink);margin-top:68px}
.lenders p{font-size:19px;color:var(--muted);line-height:38px;margin:12px auto 0;width:720px;font-weight:300}
.lender-row{position:absolute;left:170px;top:234px;width:860px;display:flex;justify-content:space-between;align-items:center;color:#222}
.lender{font-size:24px;font-weight:700;display:flex;align-items:center;gap:8px}
.lender i{width:26px;height:26px;background:#333;display:block}

/* features */
.features{position:absolute;left:0;top:1466px;width:1200px;height:383px;background:linear-gradient(180deg,#ee245f,#e81b57)}
.notch{position:absolute;left:580px;top:-1px;width:0;height:0;border-left:20px solid transparent;border-right:20px solid transparent;border-top:20px solid var(--white)}
.feature{position:absolute;width:360px;color:var(--white);padding-left:88px}
.feature-icon{position:absolute;left:0;top:-6px;width:72px;height:72px;border-radius:50%;border:2px solid rgba(255,255,255,.85);display:flex;align-items:center;justify-content:center}
.feature h3{font-size:19px;font-weight:500;text-transform:uppercase;white-space:nowrap}
.feature p{font-size:12.5px;line-height:20px;margin-top:6px;opacity:.95;width:215px}

/* how */
.how{position:absolute;left:0;top:1849px;width:1200px;height:452px;background:var(--white)}
.how h2{position:absolute;left:128px;top:50px;font-size:31px;font-weight:300;color:var(--ink);line-height:42px}
.how ul{position:absolute;left:128px;top:150px;width:440px;list-style:none}
.how li{position:relative;padding-left:28px;font-size:12.5px;line-height:19px;color:#555;margin-bottom:11px}
.how li svg{position:absolute;left:0;top:2px}
.read-more{position:absolute;left:128px;top:358px;width:122px;height:38px;border:1.5px solid #555;font-size:13px;text-align:center;line-height:35px;color:#444;letter-spacing:.5px}
.how-photo{position:absolute;left:600px;top:0;width:600px;height:452px;background:linear-gradient(135deg,#2c3440,#5a6b82 45%,#c9ccd2 70%,#3a4350)}

/* cta */
.cta{position:absolute;left:0;top:2301px;width:1200px;height:286px;background:linear-gradient(90deg,#3a3a3a,#5c5d5f 45%,#7a7a78 70%,#404040)}
.cta-shade{position:absolute;inset:0;background:rgba(0,0,0,.35)}
.cta h2{position:absolute;left:0;width:1200px;text-align:center;color:var(--white);font-weight:300;font-size:30px;top:66px}
.cta h3{position:absolute;left:0;width:1200px;text-align:center;color:var(--white);font-weight:400;font-size:35px;top:104px}
.cta .btn{position:absolute;left:488px;top:162px;width:206px;height:46px;line-height:46px;text-align:center;font-size:16px}

/* footer */
.footer{position:absolute;left:0;top:2587px;width:1200px;height:295px;background:var(--light-bg)}
.foot-col{position:absolute;top:52px}
.foot-col h4{font-size:16px;font-weight:500;color:var(--ink);margin-bottom:14px}
.foot-col a{display:block;font-size:12.5px;color:#666;text-decoration:none;line-height:25px}
.socials{display:flex;gap:10px;margin-top:2px}
.socials i{width:35px;height:35px;border-radius:50%;background:#222;display:block}
.badges{position:absolute;left:755px;top:170px;display:flex;gap:22px;align-items:center}
.badges i{display:block;background:#c9c9c9}
.copyright{position:absolute;left:0;top:2882px;width:1200px;height:69px;border-top:1px solid #e3e3e3;background:var(--white);text-align:center;line-height:69px;font-size:12px;color:#777}
</style>
</head>
<body>

<section class="hero">
  <div role="img" aria-label="Photo of a smiling driver holding up car keys from a silver car window" class="hero-shade"></div>
  <div class="brand"><i class="brand-mark"></i>Brindle</div>
  <div class="hero-note">Brindle has helped over 35,000 Australians with their finance!</div>
  <div class="hero-phone">
    <svg width="20" height="20" viewBox="0 0 24 24"><path fill="#ee245f" d="M6.6 10.8a15 15 0 0 0 6.6 6.6l2.2-2.2c.3-.3.7-.4 1-.2 1.1.4 2.3.6 3.6.6.6 0 1 .4 1 1V20c0 .6-.4 1-1 1A17 17 0 0 1 3 4c0-.6.4-1 1-1h3.5c.6 0 1 .4 1 1 0 1.3.2 2.5.6 3.6.1.3 0 .7-.2 1z"/></svg>
    1300 555 018
  </div>
  <h1 class="hero-title">How much can you save on your car loan?</h1>
  <p class="hero-sub">Comparing car loan lenders could save you thousands!</p>
  <svg class="hero-arrow" style="left:86px" width="34" height="80" viewBox="0 0 34 80"><path d="M30 2 4 40l26 38" fill="none" stroke="#fff" stroke-width="2"/></svg>
  <svg class="hero-arrow" style="left:1080px" width="34" height="80" viewBox="0 0 34 80"><path d="M4 2l26 38L4 78" fill="none" stroke="#fff" stroke-width="2"/></svg>
  <svg class="abs" style="left:582px;top:370px" width="36" height="22" viewBox="0 0 36 22"><path d="M3 3l15 15L33 3" fill="none" stroke="#fff" stroke-width="4"/></svg>
</section>

<section class="steps">
  <div class="step" style="left:152px">
    <div class="step-badge"><span>
      <svg width="44" height="54" viewBox="0 0 44 54"><path d="M3 3h26l12 12v36H3z" fill="none" stroke="#fff" stroke-width="3"/><path d="M11 20h22M11 28h22M11 36h22M11 44h14" stroke="#fff" stroke-width="3"/></svg>
    </span></div>
    <div class="step-title">Step 1</div>
    <div class="step-desc">Tell us how much you need for<br>your next car</div>
  </div>
  <div class="step" style="left:472px">
    <div class="step-badge"><span style="color:#fff;font-size:58px;font-weight:300">%</span></div>
    <div class="step-title">Step 2</div>
    <div class="step-desc">We provide lightning quick quotes<br>from our lenders</div>
  </div>
  <div class="step" style="left:789px">
    <div class="step-badge"><span>
      <svg width="66" height="40" viewBox="0 0 66 40"><path d="M6 24l6-14c1-3 3-5 7-5h28c4 0 6 2 7 5l6 14v10H6z" fill="none" stroke="#fff" stroke-width="3"/><path d="M12 22h42" stroke="#fff" stroke-width="3"/><circle cx="16" cy="28" r="3" fill="#fff"/><circle cx="50" cy="28" r="3" fill="#fff"/><path d="M10 34v4M56 34v4" stroke="#fff" stroke-width="4"/></svg>
    </span></div>
    <div class="step-title">Step 3</div>
    <div class="step-desc">Gain approval and drive away with<br>a better deal!</div>
  </div>
  <svg class="abs" style="left:380px;top:40px" width="120" height="60" viewBox="0 0 120 60"><path d="M4 50C30 16 72 10 106 26" fill="none" stroke="#d2d2d2" stroke-width="7"/><path d="M96 10l16 18-22 6z" fill="#d2d2d2"/></svg>
  <svg class="abs" style="left:690px;top:40px" width="120" height="60" viewBox="0 0 120 60"><path d="M4 50C30 16 72 10 106 26" fill="none" stroke="#d2d2d2" stroke-width="7"/><path d="M96 10l16 18-22 6z" fill="#d2d2d2"/></svg>

  <div class="tablet">
    <div class="side-icons"><i></i><i></i><i></i><i></i><i></i></div>
    <div class="home-key"></div>
    <div class="screen">
      <div class="screen-q">How much do you like to borrow?</div>
      <div class="amount">$5,000</div>
      <div class="slider"><div class="slider-knob"></div></div>
      <div class="ticks"><span>$5K</span><span>$10K</span><span>$20K</span><span>$30K</span><span>$40K</span><span>$50K</span><span>$60K</span><span>$70K</span><span>$80K</span><span>$90K</span><span>$100K</span></div>
      <span class="btn">Compare Car Loan</span>
    </div>
  </div>
</section>

<section class="lenders">
  <h2>Compare multiple lenders &amp; save on your finance. Get brindle</h2>
  <p>Comparing lenders can help you get great rates and save thousands! Compare Australia's top lenders with Brindle and save.</p>
  <div class="lender-row">
    <div class="lender">Harbourline</div>
    <div class="lender" style="font-size:15px"><i></i>Southgate Bank</div>
    <div class="lender" style="font-size:15px;font-weight:400">KEYSTONE LENDING</div>
    <div class="lender" style="font-size:13px"><i></i>Meridian</div>
    <div class="lender" style="font-weight:500">coinroo</div>
    <div class="lender">zipwell</div>
  </div>
</section>

<section class="features">
  <div class="notch"></div>
  <div class="feature" style="left:128px;top:72px">
    <div class="feature-icon"><svg width="36" height="32" viewBox="0 0 36 32" fill="none" stroke="#fff" stroke-width="2"><path d="M18 3v26M6 29h24M4 8h28M8 8l-5 11h10zM28 8l-5 11h10z"/></svg></div>
    <h3>Compare &amp; Save</h3><p>Compare and save with Brindle. Brindle will shop your deal around from multiple lenders to get you the best deal.</p>
  </div>
  <div class="feature" style="left:448px;top:72px">
    <div class="feature-icon"><svg width="36" height="34" viewBox="0 0 36 34" fill="none" stroke="#fff" stroke-width="2"><circle cx="20" cy="11" r="8"/><path d="M20 7v8M3 22h8l6 3h8c2 0 2 3 0 3h-9M3 30h22l9-8"/></svg></div>
    <h3>100% Finance</h3><p>100% finance is available to approved customers as the car is almost always sufficient security.</p>
  </div>
  <div class="feature" style="left:771px;top:72px">
    <div class="feature-icon" style="font-size:34px;color:#fff">%</div>
    <h3>Low Interest Rates</h3><p>Brindle, through its lending panel can provide you with some of the lowest rates on the market.</p>
  </div>
  <div class="feature" style="left:128px;top:222px">
    <div class="feature-icon"><svg width="34" height="28" viewBox="0 0 34 28"><path d="M3 15l10 10L31 3" fill="none" stroke="#fff" stroke-width="4"/></svg></div>
    <h3>No Obligation</h3><p>All applications with Brindle are obligation free.</p>
  </div>
  <div class="feature" style="left:448px;top:222px">
    <div class="feature-icon"><svg width="34" height="34" viewBox="0 0 34 34" fill="none" stroke="#fff" stroke-width="2"><rect x="3" y="6" width="28" height="25"/><path d="M3 13h28M10 2v7M24 2v7"/><path d="M8 18h4M15 18h4M22 18h4M8 24h4M15 24h4M22 24h4" stroke-width="3"/></svg></div>
    <h3>Same Day Approvals</h3><p>Our application process is quick &amp; easy. Brindle has the systems, technology and consultants</p>
  </div>
  <div class="feature" style="left:771px;top:222px">
    <div class="feature-icon"><svg width="30" height="34" viewBox="0 0 30 34" fill="#fff"><circle cx="15" cy="9" r="7"/><path d="M2 33c0-9 6-15 13-15s13 6 13 15z"/></svg></div>
    <h3>Australia's Top Lenders</h3><p>Brindle, through its lending panel can provide you with some of the lowest rates on the market.</p>
  </div>
</section>

<section class="how">
  <h2>How Brindle will help you find a<br>great deal on you car finance</h2>
  <ul>
    <li><svg width="14" height="14" viewBox="0 0 14 14"><circle cx="7" cy="7" r="7" fill="#ee245f"/><path d="M4 7l2 2 4-4" fill="none" stroke="#fff" stroke-width="1.6"/></svg>Understand your needs are requirements and find a tailored loan solution based on your finance goals.</li>
    <li><svg width="14" height="14" viewBox="0 0 14 14"><circle cx="7" cy="7" r="7" fill="#ee245f"/><path d="M4 7l2 2 4-4" fill="none" stroke="#fff" stroke-width="1.6"/></svg>Ascertain your borrowing power, your capacity for repayments so you always get a loan that's within your budget</li>
    <li><svg width="14" height="14" viewBox="0 0 14 14"><circle cx="7" cy="7" r="7" fill="#ee245f"/><path d="M4 7l2 2 4-4" fill="none" stroke="#fff" stroke-width="1.6"/></svg>Compare your car loan with 25+ lenders and banks so you gain the best deal from a top lender</li>
    <li><svg width="14" height="14" viewBox="0 0 14 14"><circle cx="7" cy="7" r="7" fill="#ee245f"/><path d="M4 7l2 2 4-4" fill="none" stroke="#fff" stroke-width="1.6"/></svg>Explain all fees charges and obligations up from so you know exactly what you' getting when it comes to your car loan</li>
  </ul>
  <div class="read-more">READ MORE</div>
  <div class="how-photo" role="img" aria-label="Photo of a couple signing car finance papers with a dealer in a showroom"></div>
</section>

<section class="cta">
  <div class="cta-shade" role="img" aria-label="Photo of a smiling driver holding car keys out of a car window"></div>
  <h2>Compare Australia's Top lenders with us today.</h2>
  <h3>Get Brindle!</h3>
  <span class="btn">Compare Car Loan</span>
</section>

<footer class="footer">
  <div class="foot-col" style="left:120px">
    <h4>CAR LOANS</h4>
    <a>Car Finance</a><a>Chattel Mortgage</a><a>Hire Purchase</a><a>Car Lease</a><a>Novated Leasing</a><a>Bad Credit Car Loans</a>
  </div>
  <div class="foot-col" style="left:317px">
    <h4>OTHER FINANCE</h4>
    <a>Boat Finance</a><a>Jet Ski Finance</a><a>Motorbike Finance</a><a>Financing for Ironhorse</a><a>Truck Finance</a>
  </div>
  <div class="foot-col" style="left:570px">
    <h4>RESOURCES</h4>
    <a>Send Us Your Bank Statements</a><a>Calculate Your Repayments</a><a>Finance Blog</a><a>Car Reviews</a><a>FAQs</a>
  </div>
  <div class="foot-col" style="left:808px">
    <h4>STAY IN TOUCH</h4>
    <div class="socials"><i></i><i></i><i></i><i></i></div>
  </div>
  <div class="badges">
    <i style="width:34px;height:60px;background:#f2c230"></i>
    <i style="width:120px;height:30px;border-radius:15px"></i>
    <i style="width:100px;height:30px"></i>
  </div>
</footer>
<div class="copyright">© 2016 Company Name&nbsp; All right reserved&nbsp; Term of Use</div>

</body>
</html>
```